KTR Motorhaus Automotive Repair and Service Shop

I need an informative and interactive website for my automotive service and repair shop. The website must give information about the shop, as well as the ability to make bookings and a forums page for our users to use and set up an account with us, in which we can give promotions via email. We are located in Pompano Beach Florida and our company name is KTR Motorhaus. Our color scheme is a red for accent and grey (neutral color) as a base. The design must communicate our message and be able to grow should we decide to retail parts in the future. One of the websites I take the highest inspiration from is http://www.lanvexbodyshop.example/. Although I do not have as nearly as many certifications as them. Attached are some images of our shop so you can see how clean and modern our building is, and I would like our website to match our feel. Thank you.

Target Market(s)

Automotive Enthusiasts

Industry/Entity Type

Automotive

Contact Information for Business Card

KTR Motorhaus /954 718 6402 /rohan@ktrmotorhaus.example/ 512 NE 9th St Pompano Beach FL 33062/ any other info needed please ask me

Coding

Coded - Design and coding required

Number of Pages Required

5+ page

Font styles to use
Sans Serif

Requirements
Must have
• Name, logo, contact info, location, phone number
Nice to have
• Building is very modern, would like a business card to match
Should not have
• Not to playful or vibrant

```html
<!DOCTYPE html>
<html lang="en">
<head>
<meta charset="utf-8">
<title>KTR Motorhaus — Auto Repair &amp; Service</title>
<link href="https://fonts.googleapis.com/css2?family=Poppins:wght@300;400;500;600;700&display=swap" rel="stylesheet">
<style>
:root{
  --red:#c8101c;
  --dark:#2a2a2b;
  --darker:#1e1f23;
  --ink:#1b1b1b;
  --text:#555;
  --muted:#8a8a8a;
  --light:#f2f2f2;
  --line:#e3e3e3;
  --white:#fff;
}
*{box-sizing:border-box;margin:0;padding:0}
html,body{width:1200px;height:2988px;overflow:hidden}
body{font-family:'Poppins',sans-serif;color:var(--text);background:var(--white);position:relative}
.wrap{position:absolute;left:234px;width:732px}
section,header,nav,footer{position:absolute;left:0;width:1200px}
.brand{font-weight:700;font-size:20px;color:var(--white);letter-spacing:1px;display:flex;align-items:center;gap:10px;white-space:nowrap}
.brand i{display:block;width:12px;height:12px;background:var(--red)}
/* header */
.topbar{top:0;height:109px;background:linear-gradient(#2f2f30,#242425)}
.topbar .brand{position:absolute;left:244px;top:40px}
.hours{position:absolute;left:568px;top:0;width:232px;height:46px;background:#1d1d1e;color:#fff;font-size:10px;font-weight:500;display:flex;align-items:center;justify-content:center;gap:7px;white-space:nowrap}
.booking{position:absolute;left:800px;top:0;width:400px;height:46px;background:var(--red);clip-path:polygon(22px 0,100% 0,100% 100%,0 100%,0 0);color:#fff;font-weight:600;font-size:13px;display:flex;align-items:center;padding-left:49px;gap:10px}
.call{position:absolute;left:636px;top:64px;color:#ddd;font-size:10px;display:flex;align-items:center;gap:7px;white-space:nowrap}
.call strong{font-size:18px;font-weight:500;color:#fff;letter-spacing:.3px}
.social{position:absolute;left:842px;top:64px;display:flex;gap:9px}
.social span{width:26px;height:26px;border-radius:50%;background:#151516}
/* nav */
.mainnav{top:109px;height:48px;background:linear-gradient(#fafafa,#e8e8e8);border-bottom:1px solid #ddd}
.mainnav ul{position:absolute;left:234px;top:0;display:flex;list-style:none;height:48px;align-items:center}
.mainnav li{font-size:10px;font-weight:600;color:var(--ink);padding:0 24px;border-right:1px solid #ccc;line-height:14px}
.mainnav li:last-child{border:0}
.mainnav li.active{background:var(--red);color:#fff;height:48px;line-height:48px;padding:0 38px;border:0}
/* hero */
.hero{top:157px;height:386px;background:linear-gradient(100deg,#3b4147 0%,#56606a 35%,#7a8894 60%,#49535c 100%);overflow:hidden}
.hero .photo{position:absolute;inset:0}
.hero .copy{position:absolute;left:234px;top:120px;color:#fff}
.hero .eyebrow{font-size:11px;font-weight:500}
.hero h1{font-size:31px;font-weight:700;line-height:36px;margin:2px 0 6px}
.hero h1 span{color:var(--red)}
.hero p{font-size:11.5px;line-height:16px;width:430px}
.btn{display:inline-flex;align-items:center;gap:8px;background:var(--red);color:#fff;font-size:10px;font-weight:600;border-radius:20px;padding:0 18px;height:38px}
.btn b{width:13px;height:13px;border:2px solid #fff;border-radius:50%}
.hero .btn{margin-top:18px}
.arrow{position:absolute;top:182px;width:38px;height:38px;background:rgba(255,255,255,.3);display:flex;align-items:center;justify-content:center}
.dots{position:absolute;left:611px;top:336px;display:flex;gap:5px}
.dots span{width:6px;height:6px;border:1px solid #fff;border-radius:50%}
.dots span:first-child{border-color:var(--red)}
/* headings */
.title{font-size:21px;font-weight:700;color:var(--ink);text-transform:uppercase}
.title span{color:var(--red)}
.rule{width:44px;height:2px;background:var(--ink);margin-top:10px}
.center{text-align:center}
.center .rule{margin:10px auto 0}
/* about */
.about{top:543px;height:381px}
.about .left{position:absolute;left:234px;top:58px;width:354px}
.about .left p{font-size:9px;line-height:16.3px;margin-top:20px}
.about .car{position:absolute;left:611px;top:43px;width:96px;height:272px;background:radial-gradient(ellipse at 50% 50%,#b51a20 0%,#8a1418 45%,#fff 72%)}
.about .right{position:absolute;left:734px;top:62px;width:232px}
.about h4{font-size:13px;font-weight:500;color:var(--ink)}
.about .sub{font-size:9px;margin-top:7px}
.steps{margin-top:16px;border-left:1px solid #ddd;margin-left:10px;padding-left:13px}
.steps div{position:relative;margin-bottom:20px}
.steps div::before{content:"";position:absolute;left:-19px;top:3px;width:11px;height:11px;border-radius:50%;background:#c9c9c9;border:2px solid #fff}
.steps h5{font-size:12px;font-weight:500;color:var(--red)}
.steps p{font-size:9px;line-height:16px;margin-top:4px}
/* services */
.services{top:924px;height:491px;background:var(--light)}
.services .head{top:57px}
.services .desc{font-size:9px;line-height:16px;margin-top:22px}
.cards{top:177px;display:flex;gap:18px}
.card{width:232px}
.card .img{height:138px}
.card .bar{height:40px;background:var(--red);color:#fff;font-size:10px;font-weight:600;display:flex;align-items:center;justify-content:space-between;padding:0 17px}
.services .more{top:401px;text-align:center}
/* faq */
.faq{top:1415px;height:456px}
.faq .head{top:56px}
.accordion{position:absolute;left:234px;top:130px;width:357px;border:1px solid var(--line)}
.acc{border-bottom:1px solid var(--line);padding:0 14px;height:45px;display:flex;align-items:center;justify-content:space-between;font-size:12px;font-weight:300;color:#666}
.acc:last-child{border:0}
.acc.open{height:auto;display:block;padding:12px 14px 14px}
.acc.open .q{display:flex;justify-content:space-between}
.acc.open p{font-size:8.5px;line-height:14px;margin-top:30px;color:#777}
.news{position:absolute;left:610px;top:131px;display:flex;gap:13px}
.post{width:171px}
.post .img{height:105px}
.post h6{font-size:11.5px;font-weight:500;color:var(--ink);line-height:15px;margin-top:9px}
.post .meta{font-size:6.5px;margin-top:9px;letter-spacing:.5px;color:#999}
.post .meta b{color:var(--red);font-weight:500;margin-right:10px}
/* testimonials */
.reviews{top:1871px;height:404px;background:#f2f3f5}
.reviews .head{top:47px}
.tcards{top:121px;display:flex;gap:18px}
.tcard{width:232px;height:182px;background:#fff;border:1px solid #e2e2e2;padding:16px 20px}
.tcard .top{display:flex;justify-content:space-between;font-size:20px;font-weight:700;color:#555;line-height:18px}
.stars{color:#f5a31a;font-size:12px;letter-spacing:5px}
.tcard p{font-size:8.5px;line-height:15px;margin-top:12px;color:#777}
.who{display:flex;align-items:center;gap:12px;margin-top:14px}
.avatar{width:48px;height:48px;border-radius:50%;background:linear-gradient(#b9b4ae,#6f6a66)}
.who b{display:block;font-size:11px;font-weight:600;color:var(--ink)}
.who span{font-size:10px;color:#2a6fb0}
.pager{position:absolute;left:564px;top:350px;display:flex;gap:4px}
.pager span{width:22px;height:2px;background:#2b3a55}
.pager span:first-child{background:var(--red)}
/* process */
.process{top:2275px;height:365px}
.process .head{top:57px}
.process svg{position:absolute;left:0;top:147px}
/* footer */
.footer{top:2640px;height:348px;background:var(--darker);color:#bbb}
.footer .brand{position:absolute;left:244px;top:68px}
.fphone{position:absolute;left:234px;top:150px;font-size:19px;font-weight:600;color:#9a9a9a}
.fline{position:absolute;left:234px;font-size:9px;color:#aaa}
.col{position:absolute;top:58px}
.col h6{font-size:10px;font-weight:600;color:#fff}
.col h6::after{content:"";display:block;width:32px;height:2px;background:var(--red);margin-top:7px}
.col ul{list-style:none;margin-top:22px}
.col li{font-size:8.5px;height:22.6px;color:#aaa;white-space:nowrap}
.col li::before{content:"›";margin-right:6px}
.col p{font-size:8.5px;line-height:15px;margin-top:22px;color:#aaa}
.input{width:200px;height:31px;border:1px solid #777;margin-top:12px;font-size:8px;color:#777;padding:10px 12px}
.subscribe{width:200px;height:31px;background:var(--red);color:#fff;font-size:9px;font-weight:600;text-align:center;line-height:31px;margin-top:11px}
.fdivider{position:absolute;left:234px;top:283px;width:732px;height:1px;background:#3a3b40}
.copy{position:absolute;left:234px;top:306px;font-size:8px;color:#aaa}
.fsocial{position:absolute;left:813px;top:298px;display:flex;gap:7px}
.fsocial span{width:26px;height:26px;border:1px solid #999;border-radius:50%}
</style>
</head>
<body>

<header class="topbar">
  <div class="brand"><i></i>KTR MOTORHAUS</div>
  <div class="hours">
    <svg width="11" height="11" viewBox="0 0 12 12"><circle cx="6" cy="6" r="5" fill="none" stroke="#fff" stroke-width="1.2"/><path d="M6 3v3.2l2 1.2" stroke="#fff" stroke-width="1.2" fill="none"/></svg>
    Monday-Saturday 7:00AM - 6:00PM
  </div>
  <div class="booking">BOOKING NOW
    <svg width="14" height="14" viewBox="0 0 14 14"><circle cx="7" cy="7" r="6" fill="none" stroke="#fff" stroke-width="1.6"/><path d="M5 4.5L7.5 7 5 9.5" stroke="#fff" stroke-width="1.6" fill="none"/></svg>
  </div>
  <div class="call">Call Us Now: <strong>954.718.6402</strong></div>
  <div class="social"><span></span><span></span><span></span><span></span></div>
</header>

<nav class="mainnav">
  <ul>
    <li class="active">HOME</li><li>ABOUT US</li><li>SERVICES</li><li>PRICING</li><li>GALLERY</li><li>BLOG</li><li>FAQ</li><li>CONTACT US</li>
  </ul>
</nav>

<section class="hero">
  <div class="photo" role="img" aria-label="Silver sports coupe driving fast along a coastal mountain road"></div>
  <div class="copy">
    <div class="eyebrow">WE GIVE YOU</div>
    <h1>QUALITY <span>AUTO REPAIR</span></h1>
    <p>Sea veniam lucilius neglegentur ad, an per sumo volum voluptatibus. Qui cu everti repudiare. Eam ut cibo nobis aperiam, elit qualisque at cum.</p>
    <div class="btn">READ MORE <b></b></div>
  </div>
  <div class="arrow" style="left:94px"><svg width="10" height="12"><path d="M7 1L2 6l5 5" stroke="#fff" fill="none" stroke-width="1.4"/></svg></div>
  <div class="arrow" style="left:1061px"><svg width="10" height="12"><path d="M3 1l5 5-5 5" stroke="#fff" fill="none" stroke-width="1.4"/></svg></div>
  <div class="dots"><span></span><span></span><span></span></div>
</section>

<section class="about">
  <div class="left">
    <div class="title">ABOUT <span>KTR MOTORHAUS</span></div>
    <div class="rule"></div>
    <p>Lorem ipsum dolor sit amet, consectetur adipiscing elit. Curabitur sed leo arcu. Integer eu venenatis ex. Proin ante ipsum, feugiat id blandit a, suscipit quis ex. Donec sodales eget neque quis iaculis. Cras semper metus vel lorem ultrices, non finibus diam mattis. Cras tristique eu dui eleifend aliquam. Fusce non elit sed quam commodo gravida non in odio. Vestibulum congue maximus porta. Ut dapibus neque at odio posuere, vel maximus dolor fringilla. Donec sem velit, accumsan vitae lobortis nec, scelerisque sed purus.</p>
    <p style="margin-top:14px">Sed scelerisque aliquet nibh, eu semper orci ullamcorper sit amet. Duis quis tincidunt purus. Phasellus et tortor a purus porttitor auctor non nec metus. Vivamus suscipit sapien ac nibh facilisis interdum. In tincidunt dictum elit, a laoreet ligula. Donec nec nunc tincidunt, euismod dui et, imperdiet tellus.</p>
  </div>
  <div class="car" role="img" aria-label="Red sports car seen from the side, standing upright"></div>
  <div class="right">
    <h4>What We Do</h4>
    <div class="sub">We offer full service auto repair &amp; maintenances</div>
    <div class="steps">
      <div><h5>Preventative Maintenance</h5><p>Aliquam ac laoreet neque. Nam tempus congue nisi, eget posuere mauris tristique eu.</p></div>
      <div><h5>Common Repairs</h5><p>Aliquam ac laoreet neque. Nam tempus congue nisi, eget posuere mauris tristique eu.</p></div>
      <div><h5>Brake Repair &amp; Service</h5><p>Aliquam ac laoreet neque. Nam tempus congue nisi, eget posuere mauris tristique eu.</p></div>
    </div>
  </div>
</section>

<section class="services">
  <div class="wrap center head">
    <div class="title">AUTO <span>REPAIR SERVICES</span></div>
    <div class="rule"></div>
    <p class="desc">Lorem ipsum dolor sit amet, consectetur adipiscing elit. Curabitur sed leo arcu.<br>Integer eu venenatis ex. Proin ante ipsum, feugiat id blandit a, suscipit quis ex.</p>
  </div>
  <div class="wrap cards">
    <div class="card"><div class="img" role="img" aria-label="Gloved hand checking an engine bay" style="background:linear-gradient(135deg,#2c2e31,#5a5d62 60%,#c9cdd2)"></div><div class="bar">ENGINE DIAGNOSTICS <span>›</span></div></div>
    <div class="card"><div class="img" role="img" aria-label="Hands holding a used oil filter" style="background:linear-gradient(135deg,#3a3633,#8d857c 50%,#4a4745)"></div><div class="bar">LUBE, OIL AND FILTERS <span>›</span></div></div>
    <div class="card"><div class="img" role="img" aria-label="Mechanic inspecting engine belts and hoses" style="background:linear-gradient(135deg,#2a2b2d,#6b6e72 55%,#3b4a5e)"></div><div class="bar">BELTS AND HOSES <span>›</span></div></div>
  </div>
  <div class="wrap more"><div class="btn">READ MORE <b></b></div></div>
</section>

<section class="faq">
  <div class="wrap center head">
    <div class="title">FAQ’S &amp; <span>NEWS</span></div>
    <div class="rule"></div>
  </div>
  <div class="accordion">
    <div class="acc open"><div class="q"><span>How we can help you?</span><span>−</span></div>
      <p>Lorem ipsum dolor sit amet, consectetuer adipiscing elit, sed diam nonummy nibh euismod tincidunt ut laoreet dolore magna aliquam erat volutpat. Ut wisi enim ad minim veniam, quis nostrud exerci tation ullamcorper suscipit lobortis nisl ut aliquip.</p></div>
    <div class="acc"><span>How we can help you?</span><span>+</span></div>
    <div class="acc"><span>How we can help you?</span><span>+</span></div>
    <div class="acc"><span>How we can help you?</span><span>+</span></div>
  </div>
  <div class="news">
    <div class="post"><div class="img" role="img" aria-label="Two colleagues reviewing documents at a desk" style="background:linear-gradient(135deg,#cfc9c1,#6d655d)"></div>
      <h6>Lorem ipsum dolor sit amet, consectetur adipiscing elit. Sed facilisis semper augue vel fermentum.</h6>
      <div class="meta"><b>MARA ELLISON</b>DEC 2, 2019</div></div>
    <div class="post"><div class="img" role="img" aria-label="Smiling customer at a bright home desk" style="background:linear-gradient(135deg,#e9e7e3,#8c8580)"></div>
      <h6>Cras dapibus leo tellus, id semper odio gravida eu. Aenean volutpat nibh vel justo vulputate vehicula.</h6>
      <div class="meta"><b>DEV OSTRANDER</b>DEC 2, 2019</div></div>
  </div>
</section>

<section class="reviews">
  <div class="wrap center head">
    <div class="title">OUR <span>CUSTOMERS SAYS</span></div>
    <div class="rule"></div>
  </div>
  <div class="wrap tcards">
    <div class="tcard"><div class="top"><span>”</span><span class="stars">★★★★★</span></div>
      <p>Lorem ipsum dolor sit amet, consectetur adipiscing elit. Quisque iaculis elementum eleifend. Cras malesuada vitae enim id imperdiet. Vestibulum vestibulum egestas.</p>
      <div class="who"><div class="avatar" role="img" aria-label="Customer portrait"></div><div><b>TOMAS REYNA</b><span>Client</span></div></div></div>
    <div class="tcard"><div class="top"><span>”</span><span class="stars">★★★★★</span></div>
      <p>Lorem ipsum dolor sit amet, consectetur adipiscing elit. Quisque iaculis elementum eleifend. Cras malesuada vitae enim id imperdiet. Vestibulum vestibulum egestas.</p>
      <div class="who"><div class="avatar" role="img" aria-label="Customer portrait"></div><div><b>TOMAS REYNA</b><span>Client</span></div></div></div>
    <div class="tcard"><div class="top"><span>”</span><span class="stars">★★★★★</span></div>
      <p>Lorem ipsum dolor sit amet, consectetur adipiscing elit. Quisque iaculis elementum eleifend. Cras malesuada vitae enim id imperdiet. Vestibulum vestibulum egestas.</p>
      <div class="who"><div class="avatar" role="img" aria-label="Customer portrait"></div><div><b>TOMAS REYNA</b><span>Client</span></div></div></div>
  </div>
  <div class="pager"><span></span><span></span><span></span></div>
</section>

<section class="process">
  <div class="wrap center head">
    <div class="title">OUR <span>WORKING PROCESS</span></div>
    <div class="rule"></div>
  </div>
  <svg width="1200" height="166" viewBox="0 0 1200 166" font-family="Poppins, sans-serif">
    <polygon points="247,0 467,0 506,83 467,166 243,166 287,83" fill="#2a2a2b" stroke="#fff" stroke-width="3"/>
    <polygon points="467,0 691,0 732,83 691,166 467,166 506,83" fill="#c8101c" stroke="#fff" stroke-width="3"/>
    <polygon points="691,0 916,0 953,83 916,166 691,166 732,83" fill="#2a2a2b" stroke="#fff" stroke-width="3"/>
    <g fill="none" stroke="#fff" stroke-width="1.5">
      <rect x="311" y="25" width="36" height="30"/><path d="M321 55l-6 8v-8M320 32l16 16M336 32l-16 16"/>
      <path d="M535 52v-14l5-8h26l5 8v14zM531 52h44M540 56v4M566 56v4M540 44h5M561 44h5"/>
      <path d="M760 53v-12l5-7h24l5 7v12zM756 53h42M766 28l6-6 4 4-6 6M786 26l8 4"/>
    </g>
    <g font-size="40" font-weight="700" fill="#4a4a4b"><text x="396" y="62">01</text><text x="612" y="62" fill="#e0565e">02</text><text x="835" y="62">03</text></g>
    <g font-size="12.5" fill="#fff"><text x="309" y="96">REQUEST <tspan font-weight="600">QUOTE</tspan></text><text x="533" y="96">BRING <tspan font-weight="600">YOUR VEHICLE</tspan></text><text x="758" y="96">GET <tspan font-weight="600">IT REPAIRED</tspan></text></g>
    <g font-size="9" fill="#fff"><text x="309" y="124">Lorem ipsum dolor sit amet, consec-</text><text x="309" y="140">tetur adipiscing elit. Curabitur sed</text>
      <text x="533" y="124">Lorem ipsum dolor sit amet, consec-</text><text x="533" y="140">tetur adipiscing elit. Curabitur sed</text>
      <text x="758" y="124">Lorem ipsum dolor sit amet, consec-</text><text x="758" y="140">tetur adipiscing elit. Curabitur sed</text></g>
  </svg>
</section>

<footer class="footer">
  <div class="brand"><i></i>KTR MOTORHAUS</div>
  <div class="fphone">(954) 718-6402</div>
  <div class="fline" style="top:188px">rohan@ktrmotorhaus.example</div>
  <div class="fline" style="top:213px">512 NE 9th St Pompano Beach FL 33062</div>
  <div class="col" style="left:497px"><h6>QUICK LINKS</h6><ul><li>Home</li><li>About Us</li><li>Services</li><li>Pricing</li><li>Gallery</li><li>Contact Us</li></ul></div>
  <div class="col" style="left:611px"><h6>OUR SERVICES</h6><ul><li>Performance Upgrades</li><li>Computer Diagnostics</li><li>Anti-Lock Brake Service</li><li>Air Conditioning Evac</li><li>Lube, vehicles damaged just</li><li>Engine Diagnostics Entire</li></ul></div>
  <div class="col" style="left:766px"><h6>OUR NEWSLETTER</h6>
    <p>Get in your inbox the latest News and Offers<br>From Harbor Line Works</p>
    <div class="input">Your email address</div>
    <div class="subscribe">SUBSCRIBE</div>
  </div>
  <div class="fdivider"></div>
  <div class="copy">Copyright © 2020 KTR MOTORHAUS. All Rights Reserved.</div>
  <div class="fsocial"><span></span><span></span><span></span><span></span><span></span></div>
</footer>

</body>
</html>
```